New website design for tech company

I want to redesign the current website - https://lumarekin.co/
I want it to keep the same colors/branding but I want it to resemble the look and feel of the following sites
https://www.qorvanusa.com/
https://www.pradix.com/
https://www.jumplow.com/global/us/home
https://www.kettonplc.co.uk/

The site layout

Target Market(s)

tech companies

Industry/Entity Type

tech

Number of Pages Required

2 page

Font styles to use
Serif

Colors

Designer to choose colors to be used in the design.

Requirements
Must have
• a nice updated design that looks cutting edge and innovative and the site colors can match the current logo

```html
<!DOCTYPE html>
<html lang="en">
<head>
<meta charset="utf-8">
<title>Lumarekin — Accessible Web Technologies</title>
<link rel="stylesheet" href="https://fonts.googleapis.com/css2?family=Archivo:wght@700;800&family=Lato:wght@400;700&display=swap">
<style>
:root{
  --ink:#111111;
  --muted:#555a60;
  --light:#f4f4f6;
  --dark:#1e1e1e;
  --green:#8dc63f;
  --blue:#0a57a8;
  --white:#ffffff;
}
*{box-sizing:border-box;margin:0;padding:0}
html,body{width:1200px;height:2662px;overflow:hidden}
body{position:relative;font-family:'Lato',sans-serif;color:var(--ink);background:var(--white)}
.abs{position:absolute}
.display{font-family:'Archivo',sans-serif;font-weight:800;text-transform:uppercase;letter-spacing:.5px}
.eyebrow{font-size:19px;display:flex;align-items:center;gap:6px}
.eyebrow::before{content:"";width:14px;height:14px;border:2px solid currentColor;border-radius:50%}
.link{font-size:12px;font-weight:700;text-transform:uppercase;padding-bottom:8px;border-bottom:1.5px solid currentColor;display:inline-flex;align-items:center;gap:8px}
.link svg{width:8px;height:10px}

/* header */
.site-header{left:0;top:0;width:1200px;height:84px;background:rgba(120,120,120,.55);z-index:2}
.brand{left:131px;top:28px;font-size:22px;font-weight:700;color:var(--green);display:flex;align-items:center;gap:8px}
.brand i{width:12px;height:12px;border-radius:50%;background:var(--blue);display:block}
.nav{right:121px;top:36px;display:flex;gap:34px;font-size:12px;color:var(--white);text-transform:uppercase}

/* hero */
.hero{left:0;top:0;width:1200px;height:628px;background:linear-gradient(100deg,#3a4a3a 0%,#6a6056 35%,#b7a493 60%,#8c6f58 80%,#5a4a40 100%)}
.hero-copy{left:122px;top:186px;color:var(--white);width:640px}
.hero-copy .eyebrow{font-size:17px}
.hero-copy h1{font-size:40px;line-height:48px;margin-top:10px}
.hero-copy p{font-size:12px;line-height:20px;margin-top:16px;opacity:.9;width:530px}
.hero-copy .link{color:var(--green);margin-top:52px;font-weight:400}

/* about */
.about{left:0;top:628px;width:1200px;height:212px;background:var(--light)}
.about .eyebrow{left:122px;top:60px}
.about h2{left:122px;top:98px;font-size:38px}
.intro{font-size:12px;line-height:20px;color:var(--muted)}
.intro b{font-size:19px;font-weight:400;color:var(--ink)}
.about .intro{left:596px;top:58px;width:480px}

/* mission */
.mission{left:0;top:840px;width:1200px;height:447px;background:var(--light)}
.mission-photo{left:0;top:0;width:592px;height:447px;background:linear-gradient(120deg,#e6eef2 0%,#9fb8cf 35%,#1d4f9e 60%,#0b2f72 100%)}
.mission-copy{left:684px;top:78px;width:330px}
.mission-copy h3{font-size:24px}
.mission-copy p{font-size:16px;line-height:25px;color:var(--muted);margin-top:18px}
.mission-copy .link{margin-top:80px}

/* team */
.team{left:0;top:1287px;width:1200px;height:633px;background:var(--dark);color:var(--white)}
.team .eyebrow{left:0;width:1200px;top:60px;justify-content:center}
.team h2{left:0;width:1200px;top:96px;text-align:center;font-size:38px}
.member{top:186px;width:254px;height:372px;background:var(--blue);text-align:center}
.member .photo{height:273px}
.member .role{font-size:11px;margin-top:14px;opacity:.85}
.member .name{font-size:17px;font-weight:700;margin-top:3px}
.member .social{display:flex;justify-content:center;gap:12px;margin-top:8px}
.member .social span{width:13px;height:13px;border-radius:50%;background:#dfe6ee}
.member .social span.on{background:var(--green)}

/* services */
.services{left:0;top:1920px;width:1200px;height:742px}
.world{left:160px;top:80px;width:900px;height:400px;background:radial-gradient(ellipse at center,rgba(205,216,230,.35),rgba(255,255,255,0) 70%)}
.services .eyebrow{left:111px;top:96px}
.services h2{left:111px;top:134px;font-size:38px}
.services .intro{left:584px;top:96px;width:480px}
.card{top:246px;height:231px;background:var(--white);box-shadow:0 4px 18px rgba(0,0,0,.06);padding:22px 13px}
.card h4{font-size:26px;font-weight:400;line-height:31px}
.card p{font-size:12px;line-height:20px;color:var(--muted);margin-top:24px}
.card .link{margin-top:20px;font-weight:700}
.footnote{left:0;width:1200px;top:2594px;text-align:center;font-size:12px}
</style>
</head>
<body>

<section class="hero abs" role="img" aria-label="Photo of a woman in a knit sweater working on a laptop with a coffee cup"></section>
<header class="site-header abs">
  <div class="brand abs"><i></i>Lumarekin</div>
  <nav class="nav abs"><span>About</span><span>Services</span><span>Lab</span><span>Partners</span><span>Contact us</span></nav>
</header>
<div class="hero-copy abs">
  <div class="eyebrow">Lumarekin - A subsidiary of Ferravel &amp; Co.</div>
  <h1 class="display">Ubiquitous ADA compliant<br>web technologies to<br>shift humanity forward</h1>
  <p>Lorem ipsum dolor sit amet, consectetur adipiscing elit. Amet proin ut vitae, felis. Mauris aliquet faucibus iaculis dui vitae ullamcorper ac.</p>
  <a class="link">Learn more <svg viewBox="0 0 8 10"><path d="M1 1l5 4-5 4" fill="none" stroke="currentColor" stroke-width="1.5"/></svg></a>
</div>

<section class="about abs">
  <div class="eyebrow abs">About Us</div>
  <h2 class="display abs">Who we are</h2>
  <p class="intro abs"><b>Lumarekin</b> is a web based Internet and technology agency aimed at serving, educating, and partnering with brands &amp; organizations on how their products and services can advance the disabled community through inclusion and diversity. By integrating strategies, solutions, and practices accommodating all persons, we strive to shift humanity forward with the power of technology.</p>
</section>

<section class="mission abs">
  <div class="mission-photo abs" role="img" aria-label="Photo of a business handshake overlaid with a glowing blue network"></div>
  <div class="mission-copy abs">
    <h3 class="display">Our Mission</h3>
    <p>To increase awareness and opportunities in the personal &amp; professional lives of disabled persons through technology, regardless of gender, age race or socio-economic background</p>
    <a class="link">Learn more <svg viewBox="0 0 8 10"><path d="M1 1l5 4-5 4" fill="none" stroke="currentColor" stroke-width="1.5"/></svg></a>
  </div>
</section>

<section class="team abs">
  <div class="eyebrow abs">Our Team</div>
  <h2 class="display abs">Meet our team</h2>
  <article class="member abs" style="left:208px">
    <div class="photo" role="img" aria-label="Portrait of the CEO wearing sunglasses and headphones" style="background:linear-gradient(160deg,#f2f2f2,#b9b4b0 55%,#3a5ea8)"></div>
    <div class="role">CEO</div><div class="name">Mirela</div>
    <div class="social"><span></span><span class="on"></span><span></span></div>
  </article>
  <article class="member abs" style="left:473px">
    <div class="photo" role="img" aria-label="Black and white portrait of the COO in a cap" style="background:linear-gradient(160deg,#d8d8d8,#7a7a7a 55%,#2a2a2a)"></div>
    <div class="role">COO</div><div class="name">Corwin</div>
    <div class="social"><span></span><span class="on"></span><span></span></div>
  </article>
  <article class="member abs" style="left:737px">
    <div class="photo" role="img" aria-label="Placeholder photo of a business handshake with blue network lines" style="background:linear-gradient(120deg,#e6eef2,#8fb0d0 40%,#12438f)"></div>
    <div class="role">CO</div><div class="name">Anselm</div>
    <div class="social"><span></span><span class="on"></span><span></span></div>
  </article>
</section>

<section class="services abs">
  <div class="world abs" role="img" aria-label="Faint world map in the background"></div>
  <div class="eyebrow abs">Our Services</div>
  <h2 class="display abs">What we do</h2>
  <p class="intro abs"><b>Lumarekin</b> is a web based Internet and technology agency aimed at serving, educating, and partnering with brands &amp; organizations on how their products and services can advance the disabled community through inclusion and diversity. By integrating strategies, solutions, and practices accommodating all persons, we strive to shift humanity forward with the power of technology.</p>
  <article class="card abs" style="left:110px;width:318px">
    <h4>Web &amp; Digital<br>Accessibility</h4>
    <p>Lorem ipsum dolor sit amet, consectetur adipiscing elit. Amet proin ut vitae, felis. Mauris aliquet faucibus iaculis dui vitae ullamcorper ac.</p>
    <a class="link">Learn more <svg viewBox="0 0 8 10"><path d="M1 1l5 4-5 4" fill="none" stroke="currentColor" stroke-width="1.5"/></svg></a>
  </article>
  <article class="card abs" style="left:458px;width:316px">
    <h4>Software<br>Development</h4>
    <p>Lorem ipsum dolor sit amet, consectetur adipiscing elit. Amet proin ut vitae, felis. Mauris aliquet faucibus iaculis dui vitae ullamcorper ac.</p>
    <a class="link">Learn more <svg viewBox="0 0 8 10"><path d="M1 1l5 4-5 4" fill="none" stroke="currentColor" stroke-width="1.5"/></svg></a>
  </article>
  <article class="card abs" style="left:804px;width:328px">
    <h4>Training &amp;<br>Education</h4>
    <p>Lorem ipsum dolor sit amet, consectetur adipiscing elit. Amet proin ut vitae, felis. Mauris aliquet faucibus iaculis dui vitae ullamcorper ac.</p>
    <a class="link">Learn more <svg viewBox="0 0 8 10"><path d="M1 1l5 4-5 4" fill="none" stroke="currentColor" stroke-width="1.5"/></svg></a>
  </article>
</section>
<p class="footnote abs">To be completed</p>

</body>
</html>
```